I want our new logo design to guide the colors and look of the home page. I want it to be vibrant and contemporary. We are a new religious education publishing company. I would like any colors used to describe the product below to be bright and cheerful, but also to look good with our logo colors
On our home page we are introducing a new product for second graders. The product name should look child friendly, but not silly. If there is a way to add reverence to the words FIRST RECONCILIATION and FIRST EUCHARIST, and still make it look like it is a product for children, that would be great.
The product will be called:
Little Pilgrim Learning Set for the Open Door Room
FIRST RECONCILIATION
FIRST EUCHARIST
THE PRODUCT DESCRIPTION SHOULD BE AS FOLLOWS
Field tested and designed for the special needs inclusive classroom
Kit includes high impact visuals, hands-on activities, manipulatives, games, and other teaching aids for total engagement of ALL students
Detailed catechist lesson plans to maximize learning and retention
Cost effective reusable kit
Bilingual
Somewhere it should say COMING SOON, because the product is not ready yet, but we are promoting it. I don't have a picture of this product yet, but above the product description, we need an empty box that we'll use when we're ready to upload the picture of the kit.
There should also be a statement near the product description that says: To learn more about the Little Pilgrim Set for the Open Door Room, click here.
Web page links:
About Us
Products
Resources
Contact Us
I would also like a few links to be featured on the home page:
Faith Lessons for Tomorrow's Hearts....learn more
"Where Do We Begin?"....learn more
Could It Be Something Deeper Inside?...learn more
The Dream and the Daily...learn more
Genuine Welcoming Formation
I have increased my budget and clarified my brief so that it's easier to understand. It's basically just a home page and a template for the other pages. There is no content on the other web pages that you have to work on. I just need a well designed home page and a nice template for the other pages.
Reason: I am extending the deadline for 2 days so that templates can be designed for 5 additional web pages. Please make each template a little different from the way you designed the home page. These pages can have blank picture boxes and dummy text to save you time. I am only interested in layout for the addtional pages. Thank you!
We've made a selection and wanted to thank all of you for your wonderful designs!

```html
<!DOCTYPE html>
<html lang="en">
<head>
<meta charset="utf-8">
<title>Harbor Light Catechetics – Home</title>
<link href="https://fonts.googleapis.com/css2?family=Open+Sans:ital,wght@0,300;0,400;0,600;0,700;1,400;1,600&family=Oswald:wght@500;600&family=Merriweather:ital,wght@1,700&display=swap" rel="stylesheet">
<style>
  :root {
    --red: #c9232b;
    --red-deep: #8f1519;
    --red-dark: #6e0f12;
    --yellow: #f7c61a;
    --yellow-soft: #fde38a;
    --ink: #3a3a3a;
    --muted: #777;
    --line: #e3e3e3;
    --white: #ffffff;
  }
  * { box-sizing: border-box; margin: 0; padding: 0; }
  html, body { width: 900px; height: 1200px; overflow: hidden; background: var(--white); }
  body { font-family: "Open Sans", Arial, sans-serif; color: var(--ink); }
  .page { position: relative; width: 900px; height: 1200px; overflow: hidden; }

  /* header */
  .site-header { position: absolute; top: 0; left: 0; width: 900px; height: 92px; border-bottom: 3px solid var(--red); }
  .brand { position: absolute; left: 40px; top: 22px; display: flex; align-items: center; gap: 10px; }
  .brand-dot { width: 30px; height: 30px; border-radius: 50%; background: var(--yellow); }
  .brand-name { font-size: 25px; font-weight: 700; color: var(--red); line-height: 1; }
  .brand-tagline { position: absolute; left: 80px; top: 56px; font-size: 12px; font-style: italic; color: var(--muted); }
  .main-nav { position: absolute; right: 40px; top: 30px; display: flex; gap: 4px; }
  .main-nav a { font-size: 13px; color: var(--ink); text-decoration: none; padding: 6px 11px; }
  .main-nav a.is-active { background: var(--red); color: var(--white); }

  /* hero */
  .hero { position: absolute; left: 40px; top: 108px; width: 820px; height: 330px; border: 6px solid var(--red-deep); }
  .hero-photo { position: absolute; inset: 0; background: linear-gradient(160deg, #d9c9b2 0%, #b9a48a 40%, #8e7a63 75%, #6f8a4a 100%); }
  .hero-quote { position: absolute; left: 60px; top: 14px; width: 220px; height: 270px; background: var(--yellow); transform: rotate(-2deg); padding: 22px 20px; box-shadow: 2px 3px 8px rgba(0,0,0,.25); }
  .hero-quote p { font-family: "Merriweather", Georgia, serif; font-style: italic; font-weight: 700; font-size: 20px; line-height: 1.32; color: var(--red-dark); }
  .hero-quote cite { display: block; margin-top: 10px; text-align: right; font-style: normal; font-size: 12px; font-weight: 700; color: var(--red-dark); letter-spacing: 1px; }

  /* welcome */
  .welcome { position: absolute; left: 40px; top: 468px; width: 500px; }
  .welcome h1 { font-weight: 300; font-size: 44px; color: var(--red); margin-bottom: 14px; }
  .welcome p { font-size: 12.5px; line-height: 1.55; color: #555; margin-bottom: 12px; }

  /* product promo */
  .promo { position: absolute; left: 570px; top: 480px; width: 290px; height: 380px; background: linear-gradient(180deg, #d8282f 0%, var(--red) 55%, #b01d24 100%); padding: 42px 20px 16px; color: var(--white); box-shadow: 0 2px 8px rgba(0,0,0,.2); }
  .promo-badge { position: absolute; left: -16px; top: -14px; width: 90px; height: 52px; background: var(--yellow); transform: rotate(-14deg); display: flex; align-items: center; justify-content: center; text-align: center; font-family: "Oswald", Arial, sans-serif; font-weight: 600; font-size: 14px; line-height: 1.05; color: var(--red-dark); box-shadow: 1px 2px 5px rgba(0,0,0,.25); }
  .promo-title { font-style: italic; font-weight: 600; font-size: 15px; line-height: 1.25; color: var(--yellow-soft); margin-bottom: 6px; }
  .promo-sacraments { font-family: "Oswald", Arial, sans-serif; font-weight: 600; font-size: 23px; line-height: 1.15; letter-spacing: .5px; margin-bottom: 8px; }
  .promo-list { list-style: none; border-top: 1px solid rgba(255,255,255,.35); }
  .promo-list li { font-size: 10.5px; line-height: 1.35; padding: 4px 0 4px 12px; border-bottom: 1px solid rgba(255,255,255,.35); position: relative; color: var(--yellow-soft); }
  .promo-list li::before { content: ""; position: absolute; left: 0; top: 9px; width: 5px; height: 5px; background: var(--yellow); }
  .promo-more { margin-top: 8px; font-size: 10.5px; line-height: 1.35; }
  .promo-more a { display: inline-block; margin-top: 4px; background: var(--yellow); color: var(--red-dark); font-weight: 700; font-size: 10px; padding: 2px 8px; text-decoration: none; }

  /* feature links */
  .features { position: absolute; left: 40px; top: 888px; width: 820px; display: flex; gap: 20px; }
  .feature { width: 148px; text-align: center; }
  .feature-photo { width: 148px; height: 98px; border: 3px solid var(--white); box-shadow: 0 1px 5px rgba(0,0,0,.3); }
  .feature:nth-child(1) .feature-photo { background: linear-gradient(135deg, #c9b9a6, #8d9cb0); }
  .feature:nth-child(2) .feature-photo { background: linear-gradient(135deg, #d6c3a8, #a58463); }
  .feature:nth-child(3) .feature-photo { background: linear-gradient(135deg, #bfcad4, #8a98a8); }
  .feature:nth-child(4) .feature-photo { background: linear-gradient(135deg, #e0cbb0, #b78f6d); }
  .feature:nth-child(5) .feature-photo { background: linear-gradient(135deg, #d4c0a8, #9c8a78); }
  .feature-caption { font-size: 10px; color: var(--ink); margin-top: 8px; line-height: 1.3; height: 26px; }
  .feature-more { display: inline-block; font-size: 9px; color: var(--white); background: var(--red); padding: 2px 10px; text-decoration: none; }

  /* footer */
  .site-footer { position: absolute; left: 0; top: 1062px; width: 900px; height: 138px; background: var(--red); border-top: 4px solid var(--red-deep); }
  .footer-col { position: absolute; top: 14px; }
  .footer-col h2 { font-size: 18px; font-weight: 400; color: var(--white); margin-bottom: 6px; }
  .footer-links { list-style: none; }
  .footer-links li { font-size: 10.5px; color: var(--yellow-soft); line-height: 1.6; }
  .footer-links li::before { content: "› "; color: var(--white); }
  .col-links { left: 60px; }
  .col-follow { left: 300px; }
  .social { display: flex; gap: 8px; margin-top: 4px; }
  .social span { width: 26px; height: 26px; border-radius: 50%; background: var(--white); opacity: .9; }
  .col-help { left: 520px; }
  .col-help h2 { font-size: 13px; font-weight: 700; color: var(--yellow); letter-spacing: 1px; }
  .help-phone { font-size: 22px; color: var(--white); }
  .footer-brand { position: absolute; left: 690px; top: 30px; display: flex; align-items: center; gap: 8px; }
  .footer-brand .brand-dot { width: 22px; height: 22px; }
  .footer-brand .brand-name { font-size: 17px; color: var(--yellow); }
  .footer-bottom { position: absolute; left: 0; bottom: 0; width: 900px; height: 30px; background: var(--red-deep); font-size: 10.5px; color: var(--white); padding: 8px 60px; }
</style>
</head>
<body>
<div class="page">

  <header class="site-header">
    <div class="brand">
      <span class="brand-dot"></span>
      <span class="brand-name">Harbor Light Catechetics</span>
    </div>
    <div class="brand-tagline">a new approach to catechesis</div>
    <nav class="main-nav">
      <a href="#" class="is-active">Home</a>
      <a href="#">About Us</a>
      <a href="#">Products</a>
      <a href="#">Resources</a>
      <a href="#">Contact Us</a>
    </nav>
  </header>

  <section class="hero">
    <div class="hero-photo" role="img" aria-label="Photo of a small child walking barefoot along a sunny garden path"></div>
    <blockquote class="hero-quote">
      <p>Train up a child in the way he should go, and when he is old he will not depart from it.</p>
      <cite>– PROVERBS 22:6</cite>
    </blockquote>
  </section>

  <section class="welcome">
    <h1>Welcome</h1>
    <p>Aliquam congue fermentum nisl. Mauris accumsan nulla vel diam. Sed in lacus ut enim adipiscing aliquet.</p>
    <p>Nulla venenatis. In pede mi, aliquet sit amet, euismod in, auctor ut, ligula. Aliquam dapibus tincidunt metus. Praesent justo dolor, lobortis quis, lobortis dignissim, pulvinar ac, lorem. Vestibulum sed ante. Donec sagittis euismod purus.</p>
    <p>Lorem ipsum dolor sit amet, consectetuer adipiscing elit. Praesent vestibulum molestie lacus. Aenean nonummy hendrerit mauris. Phasellus porta. Fusce suscipit varius mi. Cum sociis natoque penatibus et magnis dis parturient montes, nascetur ridiculus mus. Nulla dui. Fusce feugiat malesuada odio.</p>
    <p>Mauris accumsan nulla vel diam. Sed in lacus ut enim adipiscing aliquet.</p>
    <p>Nulla venenatis. In pede mi, aliquet sit amet, euismod in, auctor ut, ligula. Aliquam dapibus tincidunt metus. Praesent justo dolor, lobortis quis, lobortis dignissim, pulvinar.</p>
  </section>

  <aside class="promo">
    <div class="promo-badge">COMING<br>SOON</div>
    <p class="promo-title">Little Pilgrim Learning Set for the Open Door Room</p>
    <p class="promo-sacraments">FIRST RECONCILIATION<br>FIRST EUCHARIST</p>
    <ul class="promo-list">
      <li>Field tested and designed for the special needs inclusive classroom</li>
      <li>Kit includes high impact visuals, hands-on activities, manipulatives, games, and other teaching aids for total engagement of ALL students</li>
      <li>Detailed catechist lesson plans to maximize learning and retention</li>
      <li>Cost effective reusable kit</li>
      <li>Bilingual</li>
    </ul>
    <p class="promo-more">To learn more about the Little Pilgrim Set for the Open Door Room, <a href="#">click here</a></p>
  </aside>

  <section class="features">
    <article class="feature">
      <div class="feature-photo" role="img" aria-label="Photo of children learning together in a classroom"></div>
      <p class="feature-caption">Faith Lessons for Tomorrow's Hearts</p>
      <a class="feature-more" href="#">learn more</a>
    </article>
    <article class="feature">
      <div class="feature-photo" role="img" aria-label="Photo of a child thinking at a desk"></div>
      <p class="feature-caption">"Where Do We Begin?"</p>
      <a class="feature-more" href="#">learn more</a>
    </article>
    <article class="feature">
      <div class="feature-photo" role="img" aria-label="Photo of a child working with a teacher"></div>
      <p class="feature-caption">Could It Be Something Deeper Inside?</p>
      <a class="feature-more" href="#">learn more</a>
    </article>
    <article class="feature">
      <div class="feature-photo" role="img" aria-label="Photo of a group of children in a lesson"></div>
      <p class="feature-caption">The Dream and the Daily</p>
      <a class="feature-more" href="#">learn more</a>
    </article>
    <article class="feature">
      <div class="feature-photo" role="img" aria-label="Photo of a catechist with young students"></div>
      <p class="feature-caption">Genuine Welcoming Formation</p>
      <a class="feature-more" href="#">learn more</a>
    </article>
  </section>

  <footer class="site-footer">
    <div class="footer-col col-links">
      <h2>Useful Links</h2>
      <ul class="footer-links">
        <li>Parish catechist resources</li>
        <li>Family faith at home</li>
        <li>Teaching tips and guides</li>
      </ul>
    </div>
    <div class="footer-col col-follow">
      <h2>Follow Us</h2>
      <div class="social" aria-label="Social links">
        <span></span><span></span><span></span>
      </div>
    </div>
    <div class="footer-col col-help">
      <h2>ONLINE HELP</h2>
      <p class="help-phone">1.800.555.01.42</p>
    </div>
    <div class="footer-brand">
      <span class="brand-dot"></span>
      <span class="brand-name">Harbor Light Catechetics</span>
    </div>
    <div class="footer-bottom">© Copyright 2011 &nbsp;|&nbsp; Harbor Light Catechetics &nbsp;|&nbsp; All Rights Reserved</div>
  </footer>

</div>
</body>
</html>
```